Letterhead

We would like to use the logo attached as a new letterhead. Our problem is that we think the dark blue background is too much. We'd like a sleek, professional letterhead, and we'd like at least five options to choose from. I've also uploaded our old letterhead for reference of the style we're going for.

```html
<!DOCTYPE html>
<html lang="en">
<head>
<meta charset="utf-8">
<title>Harbor Line Strategies — Letterhead</title>
<link href="https://fonts.googleapis.com/css2?family=Cinzel:wght@500&family=Montserrat:wght@400;500&display=swap" rel="stylesheet">
<style>
  :root {
    --backdrop: #ececec;
    --paper: #ffffff;
    --navy: #1f2c4d;
    --gold: #b8955a;
    --ink: #3a3d44;
    --ink-soft: #5a5e66;
    --ink-blue: #2b3fae;
    --signature-fill: #e3e7f5;
  }
  * { box-sizing: border-box; margin: 0; padding: 0; }
  html, body {
    width: 1200px;
    height: 900px;
    overflow: hidden;
    background: var(--backdrop);
  }
  .letterhead {
    position: absolute;
    left: 300px;
    top: 26px;
    width: 600px;
    height: 848px;
    background: var(--paper);
    box-shadow: 0 2px 14px rgba(0,0,0,0.08);
    font-family: "Montserrat", sans-serif;
    color: var(--ink);
  }
  .brand {
    position: absolute;
    left: 58px;
    top: 64px;
    display: flex;
    align-items: center;
    gap: 12px;
  }
  .brand-mark {
    width: 14px;
    height: 14px;
    background: var(--gold);
  }
  .brand-name {
    font-family: "Cinzel", serif;
    font-weight: 500;
    font-size: 19px;
    letter-spacing: 1.5px;
    color: var(--navy);
    line-height: 1;
  }
  .letter-body {
    position: absolute;
    left: 58px;
    top: 262px;
    width: 486px;
    font-size: 9.6px;
    line-height: 1.45;
    color: var(--ink);
  }
  .letter-body p { margin-bottom: 14px; }
  .sign-off {
    position: absolute;
    left: 58px;
    top: 608px;
  }
  .signature {
    width: 118px;
    height: 34px;
    background: var(--signature-fill);
    border-radius: 3px;
  }
  .signer-role {
    margin-top: 4px;
    font-size: 10px;
    color: var(--ink-soft);
  }
  .contact {
    position: absolute;
    right: 58px;
    bottom: 96px;
    width: 300px;
    text-align: right;
    font-family: "Cinzel", serif;
    font-size: 8.6px;
    letter-spacing: 0.4px;
    line-height: 1.5;
    color: var(--navy);
  }
  .contact-rule {
    height: 1px;
    background: var(--gold);
    margin-bottom: 8px;
  }
</style>
</head>
<body>
  <main class="letterhead">
    <header class="brand">
      <span class="brand-mark"></span>
      <span class="brand-name">Harbor Line Strategies</span>
    </header>

    <section class="letter-body">
      <p>Letterhead samples are a great way of deciding what kind of letterhead you want to design for you and your company. The internet has a ton of great letterhead samples to browse through. Whether you want something simple, with just a couple lines of text of your business information, or something decorative and stunning, with photos and logos on the top and bottom of the page, it will be easy to find what you want, because there are samples online for basically any type of letterhead you could want.</p>
      <p>Any business could easily benefit from browsing through some letterhead samples, if only to get an idea for what kind of letterhead their company might want. Letterheads are just one of the tools that a business professional could use to help increase their customer base, and to really be memorable to everyone they write a letter to. Letterhead is quite an effective tool for marketing and advertising, but because it's such a simple and well known idea, it is often unfairly overlooked. Make sure you don't make that mistake, and make some letterhead samples of your own today.</p>
      <p>Whether you want to get new customers to remember you and become part of your clientele, or you just want to send out friendly reminders to your existing clients, customizing your own letterhead samples can really help you out. Try out some letterhead samples and you will not regret it, and I'm sure you will add a new tool to your business' arsenal of networking, marketing, and advertising tools.</p>
    </section>

    <div class="sign-off">
      <div class="signature" role="img" aria-label="Handwritten signature of Daniel Morrow in blue ink"></div>
      <p class="signer-role">company director</p>
    </div>

    <footer class="contact">
      <div class="contact-rule"></div>
      <p>210 Cedar Avenue, Suite 310 · Juneau, Alaska 99801</p>
      <p>907 555 0142 · hello@harborline.com</p>
    </footer>
  </main>
</body>
</html>
```